Tidewell Care Community Catalogue

I would like an A4 brochure designed consistent with my company branding . This can be seen at www.tidewellcare.com.au . All content is available in document below.

I've also included the brand guidelines document.

Target Market(s)

People in the community suffering from injuries & Disabilities

Industry/Entity Type

Health Service

Font styles to use

Colors
33b8a4
acd037

Requirements
Must have
• Good use of the pictures I've included.
• Brand colours & Fonts
• Consistency with brand look and feel

```html
<!DOCTYPE html>
<html lang="en">
<head>
<meta charset="utf-8">
<title>VSA – Tidewell Care</title>
<link href="https://fonts.googleapis.com/css2?family=Open+Sans:wght@700;800&family=PT+Sans:wght@400;700&display=swap" rel="stylesheet">
<style>
  :root {
    --ink: #3a3a3a;
    --heading: #111111;
    --rule-green: #1f6b3a;
    --bar-grey: #7b7b7b;
    --white: #ffffff;
    --pool-light: #7fd0e6;
    --pool-mid: #2fa7cc;
    --pool-deep: #1a6f96;
    --band-start: #2a8fcf;
    --band-mid: #5a9a6a;
    --band-end: #8a6a90;
  }
  * { margin: 0; padding: 0; box-sizing: border-box; }
  html, body { width: 849px; height: 1200px; overflow: hidden; background: var(--white); }
  body { font-family: "PT Sans", Arial, sans-serif; color: var(--ink); }
  .page { position: relative; width: 849px; height: 1200px; overflow: hidden; }

  .page-title {
    position: absolute; top: 58px; left: 0; width: 100%;
    font-family: "Open Sans", Arial, sans-serif;
    text-align: center; font-size: 50px; font-weight: 800; color: var(--heading); letter-spacing: 1px;
  }
  .title-rule {
    position: absolute; top: 140px; left: 356px; width: 137px; height: 6px; background: var(--rule-green);
  }
  .intro {
    position: absolute; top: 184px; left: 42px; width: 765px;
    font-size: 15px; line-height: 23.4px; text-align: justify; text-align-last: center;
    hyphens: auto; -webkit-hyphens: auto;
  }

  .hero-photo {
    position: absolute; top: 434px; left: 0; width: 849px; height: 368px;
    background: linear-gradient(160deg, var(--pool-light) 0%, var(--pool-mid) 50%, var(--pool-deep) 100%);
  }

  .section-bar {
    position: absolute; top: 843px; height: 36px; background: var(--bar-grey);
    color: var(--white); font-size: 12.5px; font-weight: 700; text-transform: uppercase;
    text-align: center; line-height: 15px; display: flex; align-items: center; justify-content: center;
    padding: 0 20px;
  }
  .bar-services { left: 56px; width: 349px; }
  .bar-conditions { left: 440px; width: 394px; }

  .card-type { position: absolute; left: 56px; width: 316px; }
  .card-type h3 { font-family: "Open Sans", Arial, sans-serif; font-size: 16px; font-weight: 700; color: var(--heading); margin-bottom: 6px; }
  .card-type p { font-size: 12.5px; line-height: 18.5px; hyphens: auto; -webkit-hyphens: auto; }
  .card-gold { top: 906px; }
  .card-white { top: 990px; }

  .conditions { position: absolute; top: 904px; left: 442px; width: 366px; font-size: 12.5px; }
  .conditions p { line-height: 18px; margin-bottom: 18px; hyphens: auto; -webkit-hyphens: auto; }
  .conditions ul { list-style: none; line-height: 18px; }

  .brand-band {
    position: absolute; left: 0; bottom: 0; width: 849px; height: 15px;
    background: linear-gradient(90deg, var(--band-start), var(--band-mid), var(--band-end));
  }
</style>
</head>
<body>
<main class="page">
  <h1 class="page-title">VSA</h1>
  <div class="title-rule"></div>

  <p class="intro">Few human acts are more significant than serving to protect and defend one’s country. Yet unfortunately, as returned service men and women know too well, the adverse physical, mental and emotional effects can last long after landing on home soil. As well as treatment for immediate injuries, many returned service personnel require ongoing, long-term care and multiple healthcare services for chronic pain or disability, injuries that deteriorate over time and delayed-onset conditions such as arthritis. At Tidewell Care, we are dedicated to working with the provisions of the Veterans Support Agency (VSA) to ensure that veterans receive optimal treatment without being out of pocket – we charge no gap payment for eligible clients – and help facilitate their return to living a rich, full and well civilian life. If you are eligible and wish to book an appointment, you’ll need to bring your Veteran Card in prior to seeing a practitioner. If you do not have a gold or white VSA card and would like to check whether you’re eligible, you can contact VSA on 1800 555 019.</p>

  <div class="hero-photo" role="img" aria-label="Two people doing aqua therapy exercises with foam dumbbells in a blue swimming pool"></div>

  <div class="section-bar bar-services">Tidewell Care services available to veteran card holders include:</div>
  <div class="section-bar bar-conditions">Conditions we treat</div>

  <section class="card-type card-gold">
    <h3>GOLD</h3>
    <p>Gold card holders have unlimited access to our services, according to clinical need.</p>
  </section>
  <section class="card-type card-white">
    <h3>WHITE</h3>
    <p>White card holders can also access all services, but only for treatment of specific conditions such as arthritis or degenerative conditions.</p>
  </section>

  <section class="conditions">
    <p>While a condition or injury’s eligibility for treatment under VSA provisions depends on veteran card type, common conditions treated by Tidewell Care practitioners among VSA clients include:</p>
    <ul>
      <li>Osteoarthritis</li>
      <li>Carpal Tunnel Syndrome</li>
      <li>Lumbar Spondylosis</li>
      <li>Rotator Cuff Syndrome</li>
      <li>Intervertebral Disc Prolapse</li>
      <li>Acute sprain and strain</li>
      <li>Irritable Bowel Syndrome (IBS)</li>
      <li>Posttraumatic Stress Disorder (PTSD)</li>
      <li>Depressive and anxiety disorders</li>
      <li>Alcohol or substance dependence and abuse</li>
    </ul>
  </section>

  <div class="brand-band" role="img" aria-label="Decorative multicoloured brand strip along the page foot"></div>
</main>
</body>
</html>
```